Typing Service Business Card Design

Need a new business card design for new logo update. The Keyline Crew is an outsourced typing service. We type audio / voice files into word documents. We are a professional service that is recognised in the industry over the past 15 years and have a strong connection to our brand. The final design should be professional, simple, yet effective.

Business

Contact Information for Business Card

Rosalind Varga
Director

rosalind@kbq.com.au
www.thekeylinecrewbase.com.au

```html
<!DOCTYPE html>
<html lang="en">
<head>
<meta charset="utf-8">
<title>The Keyline Crew – Business Card</title>
<link href="https://fonts.googleapis.com/css2?family=Roboto+Condensed:wght@300;400;700&display=swap" rel="stylesheet">
<style>
  :root {
    --magenta: #cc4a9c;
    --grey-line: #b9b9bb;
    --ink: #2b2b2b;
    --ink-soft: #555555;
    --rule: #3a3a3a;
    --card: #ffffff;
    --backdrop: #eceae6;
  }
  * { box-sizing: border-box; margin: 0; padding: 0; }
  html, body {
    width: 1200px; height: 1024px; overflow: hidden;
    background: var(--backdrop);
    font-family: "Roboto Condensed", "Arial Narrow", sans-serif;
    color: var(--ink);
  }
  .canvas { position: relative; width: 1200px; height: 1024px; }

  .card {
    position: absolute; left: 250px;
    width: 700px; height: 400px;
    background: var(--card);
    overflow: hidden;
    box-shadow: 0 6px 18px rgba(0,0,0,0.12);
  }
  .card--contact { top: 72px; }
  .card--brand { top: 552px; }

  .card__strip {
    position: absolute; left: 0; right: 0; bottom: 0; height: 40px;
    background: var(--magenta);
    border-top: 6px solid var(--grey-line);
  }

  /* Name lockup */
  .brand { display: flex; align-items: center; gap: 12px; }
  .brand__mark {
    width: 12px; height: 12px; background: var(--magenta); flex: none;
  }
  .brand__name {
    font-weight: 400; color: var(--ink);
    letter-spacing: 0.5px; white-space: nowrap;
  }
  .tagline {
    font-weight: 300; color: var(--ink-soft); white-space: nowrap;
  }

  /* Contact side */
  .card--contact .brand { position: absolute; left: 46px; top: 58px; }
  .card--contact .brand__name { font-size: 34px; }
  .card--contact .tagline {
    position: absolute; left: 70px; top: 106px; font-size: 19px;
  }
  .person {
    position: absolute; right: 46px; top: 40px; width: 260px; text-align: right;
  }
  .person__name {
    display: block; font-size: 24px; font-weight: 400; color: var(--ink); white-space: nowrap;
  }
  .person__role {
    display: block; font-size: 16px; font-weight: 700; color: var(--magenta);
    letter-spacing: 1px; margin-top: 4px;
  }
  .divider {
    position: absolute; left: 46px; right: 46px; top: 168px;
    height: 1px; background: var(--rule);
  }
  .contacts {
    position: absolute; left: 46px; top: 196px;
    list-style: none; display: grid; gap: 16px;
  }
  .contacts__item {
    display: flex; align-items: center; gap: 14px;
    font-size: 19px; color: var(--ink);
  }
  .contacts__icon { width: 26px; height: 26px; flex: none; }

  /* Brand side */
  .card--brand .lockup {
    position: absolute; left: 0; right: 0; top: 120px;
    display: flex; flex-direction: column; align-items: center; gap: 14px;
  }
  .card--brand .brand__name { font-size: 54px; }
  .card--brand .brand__mark { width: 16px; height: 16px; }
  .card--brand .tagline { font-size: 26px; }
</style>
</head>
<body>
<main class="canvas">

  <section class="card card--contact" aria-label="Business card, contact side">
    <div class="brand">
      <span class="brand__mark"></span>
      <span class="brand__name">The Keyline Crew</span>
    </div>
    <p class="tagline">Spoken in, typed out.</p>

    <div class="person">
      <span class="person__name">Rosalind Varga</span>
      <span class="person__role">DIRECTOR</span>
    </div>

    <div class="divider"></div>

    <ul class="contacts">
      <li class="contacts__item">
        <svg class="contacts__icon" viewBox="0 0 26 26" aria-hidden="true">
          <circle cx="13" cy="13" r="13" fill="var(--magenta)"/>
          <rect x="6.5" y="8.5" width="13" height="9" fill="none" stroke="#fff" stroke-width="1.4"/>
          <polyline points="6.5,8.5 13,14 19.5,8.5" fill="none" stroke="#fff" stroke-width="1.4"/>
        </svg>
        <span>rosalind@kbq.com.au</span>
      </li>
      <li class="contacts__item">
        <svg class="contacts__icon" viewBox="0 0 26 26" aria-hidden="true">
          <circle cx="13" cy="13" r="13" fill="var(--magenta)"/>
          <circle cx="13" cy="13" r="7" fill="none" stroke="#fff" stroke-width="1.3"/>
          <ellipse cx="13" cy="13" rx="3" ry="7" fill="none" stroke="#fff" stroke-width="1.2"/>
          <line x1="6" y1="13" x2="20" y2="13" stroke="#fff" stroke-width="1.2"/>
        </svg>
        <span>www.thekeylinecrewbase.com.au</span>
      </li>
    </ul>

    <div class="card__strip"></div>
  </section>

  <section class="card card--brand" aria-label="Business card, brand side">
    <div class="lockup">
      <div class="brand">
        <span class="brand__mark"></span>
        <span class="brand__name">The Keyline Crew</span>
      </div>
      <p class="tagline">Spoken in, typed out.</p>
    </div>

    <div class="card__strip"></div>
  </section>

</main>
</body>
</html>
```